Bright Tooth Dentistry Business Card

We need business cards for our dental office.
We are looking for a clean, elegant design

We provide dental services to children.
Our card needs to be appealing to referring dentists, parents and our team

Target Market(s)

referring dentists, parents and our team

Industry/Entity Type

Dental Clinic

Contact Information for Business Card

4816 Juniper Lane, Suite 100
Cedar Hollow, PA 15237

412-837-2961 Voice
412-837-2962 fax
info@brighttoothdentalpa.com email
www.brighttoothdentalpa.com web

Font styles to use
Sans Serif

Requirements
Must have
• White background - clean, crisp, elegant, simple
• rounded corners
• different color palate - once we come up with design, we will replace the blue with orange, green,
Nice to have
• Follow our logo typeface and colors
• then we can replace color

```html
<!DOCTYPE html>
<html lang="en">
<head>
<meta charset="UTF-8">
<title>Bright Tooth Dentistry — Business Card</title>
<link rel="stylesheet" href="https://fonts.googleapis.com/css2?family=Quicksand:wght@500;600;700&display=swap">
<style>
  :root {
    --backdrop: #1c1c1e;
    --brand-blue: #05ade6;
    --brand-orange: #f7941d;
    --ink-grey: #8f9194;
    --rule-grey: #a9abae;
    --card-white: #ffffff;
  }
  * { box-sizing: border-box; margin: 0; padding: 0; }
  html, body {
    width: 1200px; height: 1200px; overflow: hidden;
    background: var(--backdrop);
    font-family: "Quicksand", sans-serif;
  }
  .sheet {
    width: 1200px; height: 1200px;
    display: flex; flex-direction: column; align-items: center; justify-content: center;
    gap: 44px;
  }
  .card {
    position: relative;
    width: 900px; height: 514px;
    border-radius: 34px;
    overflow: hidden;
  }
  .card--front {
    background: var(--brand-blue);
    display: flex; align-items: center; justify-content: center;
  }
  .front-wordmark {
    color: var(--card-white);
    font-weight: 700;
    font-size: 60px;
    letter-spacing: 1px;
  }
  .card--back { background: var(--card-white); }
  .back-wordmark {
    position: absolute; left: 64px; top: 100px;
    color: var(--brand-orange);
    font-weight: 700;
    font-size: 42px;
    letter-spacing: 0.5px;
    white-space: nowrap;
  }
  .sparkle-cluster {
    position: absolute; right: 30px; top: 40px;
    width: 220px; height: 220px;
    border-radius: 24px;
    background: radial-gradient(circle at 55% 50%, #c3c5c8 0%, #dcdde0 55%, #f3f3f4 100%);
  }
  .rule { position: absolute; height: 2px; }
  .rule--orange { left: 64px; top: 258px; width: 470px; background: var(--brand-orange); }
  .rule--grey { left: 560px; top: 318px; width: 280px; background: var(--rule-grey); }
  .contact-list {
    position: absolute; left: 64px; top: 282px;
    list-style: none;
    color: var(--ink-grey);
    font-weight: 600;
    font-size: 24px;
    line-height: 40px;
  }
  .contact-list li { display: flex; align-items: center; gap: 16px; }
  .contact-icon { width: 22px; height: 22px; flex: none; }
  .address {
    position: absolute; right: 60px; top: 336px;
    text-align: right;
    color: var(--ink-grey);
    font-style: normal;
    font-weight: 600;
    font-size: 24px;
    line-height: 36px;
  }
</style>
</head>
<body>
<main class="sheet">

  <section class="card card--front" aria-label="Card front">
    <h1 class="front-wordmark">Bright Tooth Dentistry</h1>
  </section>

  <section class="card card--back" aria-label="Card back">
    <h2 class="back-wordmark">Bright Tooth Dentistry</h2>
    <div class="sparkle-cluster" role="img" aria-label="Cluster of grey four-point sparkle stars"></div>

    <div class="rule rule--orange"></div>
    <div class="rule rule--grey"></div>

    <ul class="contact-list">
      <li>
        <svg class="contact-icon" viewBox="0 0 24 24" aria-hidden="true"><path fill="#f7941d" d="M6.6 2.5l3 3.2-1.8 2.4c1.2 2.6 3.4 4.8 6 6l2.4-1.8 3.2 3-2 3.7C10 18.6 5.4 14 3 6.6z"/></svg>
        <span>412-837-2961</span>
      </li>
      <li>
        <svg class="contact-icon" viewBox="0 0 24 24" aria-hidden="true"><rect x="6" y="3" width="12" height="6" fill="#f7941d"/><rect x="2" y="9" width="20" height="9" rx="2" fill="#f7941d"/><rect x="6" y="15" width="12" height="6" fill="#fff" stroke="#f7941d" stroke-width="2"/></svg>
        <span>412-837-2962</span>
      </li>
      <li>
        <svg class="contact-icon" viewBox="0 0 24 24" aria-hidden="true"><rect x="2" y="5" width="20" height="14" fill="#f7941d"/><path d="M2 5l10 8 10-8" fill="none" stroke="#fff" stroke-width="2"/></svg>
        <span>info@brighttoothdentalpa.com</span>
      </li>
      <li>
        <svg class="contact-icon" viewBox="0 0 24 24" aria-hidden="true"><circle cx="12" cy="12" r="10" fill="#f7941d"/><path d="M2 12h20M12 2c-4 5-4 15 0 20M12 2c4 5 4 15 0 20" fill="none" stroke="#fff" stroke-width="1.5"/></svg>
        <span>www.brighttoothdentalpa.com</span>
      </li>
    </ul>

    <address class="address">
      4816 Juniper Lane, Suite 240<br>
      Cedar Hollow, PA 15237
    </address>
  </section>

</main>
</body>
</html>
```